Hack my website! Blue Harbor needs a site

We hack stuff. No joke, that is what we do, but we are the good guys!

We do security consulting, specifically offensive security. The technical term is "Penetration Testing", but you probably know it as "hacking". Companies hire us to break in before the bad guys do. (I have a very cool job :) ).

I need a web site to describe our offerings and connect with clients.

I've included my business card and logo so you can understand what I'm looking for on the website and the color scheme.

Tag line:
Offensive Services from Offensive Minds

Target Market(s)

Medium to large businesses

Industry/Entity Type

Computer Security

Coding

Coded - Design and coding required

Number of Pages Required

2 page

Font styles to use
Sans Serif

Colors

Designer to choose colors to be used in the design.

Requirements
Must have
• Flat, clean, professional look
Nice to have
• Bonus for bootstrap. See the uploaded logo for the current colors. I'd really like this to look decent on a phone too.
Should not have
• 1. Black background
• 2. The business card is to show the colors and theme so far. Please, do NOT just slam that into the middle of the site since it doesn't make sense. It feels odd that I have to say that, but I've received multiple submissions where people have done this.

```html
<!DOCTYPE html>
<html lang="en">
<head>
<meta charset="utf-8">
<title>Blue Harbor — Offensive Services from Offensive Minds</title>
<link href="https://fonts.googleapis.com/css2?family=Open+Sans:wght@400;600;700&display=swap" rel="stylesheet">
<style>
  :root {
    --brand-red: #d0202a;
    --ink: #1f1f1f;
    --muted: #6d6d6d;
    --line: #cfcfcf;
    --band: #f2f2f2;
    --footer: #ececec;
    --white: #ffffff;
    --arrow: #a9a9a9;
    --social: #2b2b2b;
  }
  * { box-sizing: border-box; margin: 0; padding: 0; }
  html, body { width: 1200px; height: 2222px; overflow: hidden; }
  body {
    position: relative;
    background: var(--white);
    font-family: "Open Sans", Arial, sans-serif;
    color: var(--ink);
  }

  /* Header */
  .site-header { position: absolute; left: 0; top: 0; width: 1200px; height: 141px; background: var(--white); }
  .brand { position: absolute; left: 131px; top: 50px; display: flex; align-items: center; gap: 12px; }
  .brand-mark { width: 22px; height: 22px; background: var(--brand-red); }
  .brand-name { font-size: 24px; font-weight: 600; letter-spacing: 5px; color: var(--brand-red); text-transform: uppercase; }
  .phone { position: absolute; right: 133px; top: 35px; font-size: 20px; display: flex; align-items: center; gap: 8px; }
  .main-nav { position: absolute; right: 133px; top: 98px; display: flex; gap: 35px; font-size: 14px; }
  .main-nav a { color: var(--ink); text-decoration: none; }
  .main-nav a.is-current { color: var(--brand-red); }

  /* Hero */
  .hero { position: absolute; left: 0; top: 141px; width: 1200px; height: 472px; }
  .hero-visual {
    position: absolute; inset: 0;
    background: linear-gradient(90deg, #f0a33c 0%, #d6c7a8 22%, #9fd7d8 48%, #7fd6d8 75%, #a9e6e6 100%);
  }
  .hero-tagline {
    position: absolute; left: 256px; top: 209px; width: 688px; height: 56px;
    background: rgba(255,255,255,0.78);
    color: var(--brand-red); font-size: 35px; font-weight: 600;
    display: flex; align-items: center; justify-content: center;
  }
  .slider-arrow {
    position: absolute; width: 25px; height: 32px; background: var(--arrow);
    display: flex; align-items: center; justify-content: center; opacity: .85;
  }
  .hero .slider-arrow { top: 220px; }
  .slider-arrow.prev { left: 0; }
  .slider-arrow.next { right: 0; }

  /* Offerings */
  .section-title { position: absolute; left: 0; width: 1200px; text-align: center; color: var(--brand-red); font-size: 35px; font-weight: 600; }
  .offerings-title { top: 682px; }
  .offerings-intro { position: absolute; left: 140px; top: 736px; width: 920px; text-align: center; font-size: 17px; line-height: 23px; }
  .offering { position: absolute; width: 300px; text-align: center; }
  .offering-icon {
    width: 96px; height: 96px; margin: 0 auto; border-radius: 50%;
    background: var(--brand-red); display: flex; align-items: center; justify-content: center;
  }
  .offering-name { margin: 21px auto 0; width: 240px; color: var(--brand-red); font-size: 18px; font-weight: 400; line-height: 24px; min-height: 48px; }
  .offering-text { margin: 16px auto 0; width: 290px; color: var(--muted); font-size: 11px; line-height: 16px; min-height: 48px; }
  .read-more {
    display: inline-block; margin-top: 16px; width: 89px; height: 36px; line-height: 34px;
    border: 1px solid var(--line); color: var(--muted); font-size: 11px; text-decoration: none;
  }

  /* Resources */
  .resources { position: absolute; left: 0; top: 1477px; width: 1200px; height: 649px; background: var(--band); }
  .resources-title { top: 90px; }
  .resources .slider-arrow { top: 337px; }
  .resource-card { position: absolute; top: 163px; width: 298px; height: 384px; background: var(--white); }
  .resource-visual { width: 298px; height: 193px; }
  .resource-body { padding: 26px 22px 0; }
  .resource-title { font-size: 16.5px; font-weight: 400; line-height: 23px; }
  .resource-date { margin-top: 16px; font-size: 10px; color: var(--muted); }
  .resource-text { margin-top: 8px; font-size: 11px; line-height: 16px; color: var(--muted); }

  /* Footer */
  .site-footer { position: absolute; left: 0; top: 2126px; width: 1200px; height: 96px; background: var(--footer); border-top: 1px solid #dcdcdc; }
  .footer-nav { position: absolute; left: 132px; top: 23px; font-size: 12px; display: flex; gap: 10px; }
  .footer-nav a { color: var(--ink); text-decoration: none; }
  .copyright { position: absolute; left: 132px; top: 53px; font-size: 11px; color: var(--ink); }
  .social { position: absolute; right: 133px; top: 29px; display: flex; gap: 13px; }
  .social span { width: 36px; height: 36px; border-radius: 50%; background: var(--social); display: block; }
</style>
</head>
<body>

<header class="site-header">
  <div class="brand"><span class="brand-mark"></span><span class="brand-name">Blue Harbor</span></div>
  <div class="phone">
    <svg width="10" height="16" viewBox="0 0 10 16"><rect x="1" y="1" width="8" height="14" rx="1.5" fill="none" stroke="#1f1f1f" stroke-width="1.6"/><circle cx="5" cy="12.5" r="0.9" fill="#1f1f1f"/></svg>
    555. 014. 2277
  </div>
  <nav class="main-nav">
    <a class="is-current" href="#">Home</a>
    <a href="#">About Us</a>
    <a href="#">Services</a>
    <a href="#">Resources</a>
    <a href="#">Contact Us</a>
  </nav>
</header>

<section class="hero">
  <div class="hero-visual" role="img" aria-label="Photo of a hand touching a glowing padlock surrounded by technology icons"></div>
  <div class="hero-tagline">Offensive Services from Offensive Minds</div>
  <span class="slider-arrow prev"><svg width="10" height="16" viewBox="0 0 10 16"><path d="M8 1 2 8l6 7" fill="none" stroke="#fff" stroke-width="1.5"/></svg></span>
  <span class="slider-arrow next"><svg width="10" height="16" viewBox="0 0 10 16"><path d="M2 1l6 7-6 7" fill="none" stroke="#fff" stroke-width="1.5"/></svg></span>
</section>

<h2 class="section-title offerings-title">Offerings</h2>
<p class="offerings-intro">Red Team Adversary Simulation - A goal based assessment where we attack just like a real world adversary. This includes external attacks and targeted phishing to demonstrate the real risk to your data.</p>

<div class="offering" style="left:128px; top:817px;">
  <div class="offering-icon">
    <svg width="50" height="50" viewBox="0 0 50 50" font-family="Open Sans, sans-serif" font-weight="700" font-size="15" fill="#fff"><text x="9" y="15">100</text><text x="3" y="30">1010</text><text x="7" y="45">01</text></svg>
  </div>
  <h3 class="offering-name">Internal Pivot Assessment &amp; Post Exploitation</h3>
  <p class="offering-text">We start as a low privileged users and attempted to move through the network in an attempt to access the data the matters to you.</p>
  <a class="read-more" href="#">Read more</a>
</div>

<div class="offering" style="left:450px; top:817px;">
  <div class="offering-icon">
    <svg width="48" height="48" viewBox="0 0 48 48" fill="none" stroke="#fff" stroke-width="1.8"><rect x="14" y="14" width="20" height="20"/><rect x="19" y="19" width="10" height="10"/><path d="M19 14V6M24 14V4M29 14V6M19 34v8M24 34v10M29 34v8M14 19H6M14 24H4M14 29H6M34 19h8M34 24h10M34 29h8"/></svg>
  </div>
  <h3 class="offering-name">Advanced Product, Hardware &amp; RF Testing</h3>
  <p class="offering-text">This a highly customized assessment designed for you and your hardware. Depending on the product we will analyze custom RF protocols, reverse...</p>
  <a class="read-more" href="#">Read more</a>
</div>

<div class="offering" style="left:771px; top:817px;">
  <div class="offering-icon">
    <svg width="30" height="48" viewBox="0 0 30 48" fill="none" stroke="#fff" stroke-width="3"><rect x="3" y="3" width="24" height="42" rx="3"/><path d="M3 9h24M3 38h24"/></svg>
  </div>
  <h3 class="offering-name">Mobile Application Assessment</h3>
  <p class="offering-text">We look at your mobile application and the associated infrastructure to find configuration weaknesses, server-side issues, insecure authentication and access ...</p>
  <a class="read-more" href="#">Read more</a>
</div>

<div class="offering" style="left:128px; top:1137px;">
  <div class="offering-icon">
    <svg width="50" height="50" viewBox="0 0 50 50" fill="none" stroke="#fff" stroke-width="2.4"><circle cx="30" cy="20" r="13"/><path d="M20 30 5 45"/><circle cx="30" cy="20" r="4"/><path d="M30 14v2M24 20h2M34 20h2M26 16l2 2M34 16l-2 2M26 25l2-2M34 25l-2-2"/></svg>
  </div>
  <h3 class="offering-name">External Penetration Testing</h3>
  <p class="offering-text">This includes vulnerability scans of the public facing systems where we manually verify issues and exploit any issues found.</p>
  <a class="read-more" href="#">Read more</a>
</div>

<div class="offering" style="left:450px; top:1137px;">
  <div class="offering-icon"></div>
  <h3 class="offering-name">Internal Penetration Testing</h3>
  <p class="offering-text">This includes port scans and vulnerability scans of the internal network. We validate the results and look for issues that aren't found by scanners.</p>
  <a class="read-more" href="#">Read more</a>
</div>

<div class="offering" style="left:771px; top:1137px;">
  <div class="offering-icon">
    <svg width="50" height="50" viewBox="0 0 50 50" fill="none" stroke="#fff" stroke-width="2.4"><path d="M21 4h8l1 6 5 2 5-4 6 6-4 5 2 5 6 1v8l-6 1-2 5 4 5-6 6-5-4-5 2-1 6h-8l-1-6-5-2-5 4-6-6 4-5-2-5-6-1v-8l6-1 2-5-4-5 6-6 5 4 5-2z"/><circle cx="25" cy="25" r="8"/></svg>
  </div>
  <h3 class="offering-name">Web Application Penetration Testing</h3>
  <p class="offering-text">Our team will perform and in-depth analysis of your web application to find vulnerabilities related to programming errors...</p>
  <a class="read-more" href="#">Read more</a>
</div>

<section class="resources">
  <h2 class="section-title resources-title">Resources</h2>
  <span class="slider-arrow prev"><svg width="10" height="16" viewBox="0 0 10 16"><path d="M8 1 2 8l6 7" fill="none" stroke="#fff" stroke-width="1.5"/></svg></span>
  <span class="slider-arrow next"><svg width="10" height="16" viewBox="0 0 10 16"><path d="M2 1l6 7-6 7" fill="none" stroke="#fff" stroke-width="1.5"/></svg></span>

  <article class="resource-card" style="left:132px;">
    <div class="resource-visual" role="img" aria-label="Photo of hands typing code on a laptop beside a coffee cup" style="background:linear-gradient(135deg,#173a4f,#2f5f74 55%,#c9c9c4);"></div>
    <div class="resource-body">
      <h3 class="resource-title">Pellentesque a imperdiet dolor, et auctor est sollicitudin.</h3>
      <p class="resource-date">3 October, 2017</p>
      <p class="resource-text">Maecenas consequat justo enim, ac mattis massa imperdiet quis. Fusce eget neque elit. Sed augue orci, elementum in magna congue, tinci.</p>
    </div>
  </article>

  <article class="resource-card" style="left:451px;">
    <div class="resource-visual" role="img" aria-label="Photo of a person using a tablet with glowing padlock graphics" style="background:linear-gradient(135deg,#1c3560,#3f7fa8 55%,#9bd3e6);"></div>
    <div class="resource-body">
      <h3 class="resource-title">Pellentesque a imperdiet dolor, et auctor est sollicitudin.</h3>
      <p class="resource-date">3 October, 2017</p>
      <p class="resource-text">Maecenas consequat justo enim, ac mattis massa imperdiet quis. Fusce eget neque elit. Sed augue orci, elementum in magna congue, tinci.</p>
    </div>
  </article>

  <article class="resource-card" style="left:770px;">
    <div class="resource-visual" role="img" aria-label="Photo of a businessman holding a glowing shield with a padlock" style="background:linear-gradient(135deg,#d8d8d8,#8d8d8d 55%,#e4e4e4);"></div>
    <div class="resource-body">
      <h3 class="resource-title">Pellentesque a imperdiet dolor, et auctor est sollicitudin.</h3>
      <p class="resource-date">3 October, 2017</p>
      <p class="resource-text">Maecenas consequat justo enim, ac mattis massa imperdiet quis. Fusce eget neque elit. Sed augue orci, elementum in magna congue, tinci.</p>
    </div>
  </article>
</section>

<footer class="site-footer">
  <nav class="footer-nav">
    <a href="#">Home</a><span>|</span>
    <a href="#">About Us</a><span>|</span>
    <a href="#">Services</a><span>|</span>
    <a href="#">Resources</a><span>|</span>
    <a href="#">Contact Us</a>
  </nav>
  <p class="copyright">Copyright &copy; 2017 Blue Harbor. All rights reserved.</p>
  <div class="social" aria-label="Social links">
    <span></span><span></span><span></span>
  </div>
</footer>

</body>
</html>
```